Ward Compass Business Card Design*

We need a business card design for our company Ward Compass. Our company is specialized in providing online consulting services regarding medical institutions, hospitals and doctors. We work with patients worldwide looking to choose between healthcare providers. We have a website you may use as a reference, where we list doctors and clinics worldwide. So we target Medical providers as well as patients worldwide.
Target Market(s)
Medical Providers and patients around the world
Industry/Entity Type
Medical
Contact Information for Business Card
Salma Derkaoui
CEO
+90 612 348 2071
info@wardcompass-example.com
www.wardcompass-example.com
14 Annakhil 3 H.R.B. Rabat, Morocco
Requirements
Must have
- Company logo/name on one full side, personal info and smaller logo and company name on the other side.
Nice to have
- Smart and elegant design

```html
<!DOCTYPE html>
<html lang="en">
<head>
<meta charset="utf-8">
<title>Ward Compass – Business Card</title>
<link rel="stylesheet" href="https://fonts.googleapis.com/css2?family=Montserrat:wght@300;400&family=Roboto:wght@300;400;900&display=swap">
<style>
  :root {
    --navy: #163a66;
    --grey-name: #7a7a7a;
    --ink: #2b2b2b;
    --paper: #ffffff;
    --backdrop: #e9eaec;
  }
  * { box-sizing: border-box; margin: 0; padding: 0; }
  html, body { width: 1200px; height: 900px; overflow: hidden; }
  body {
    background: var(--backdrop);
    font-family: "Roboto", Arial, sans-serif;
    position: relative;
  }
  .card {
    position: absolute;
    left: 250px;
    width: 700px;
    height: 400px;
    box-shadow: 0 6px 18px rgba(0,0,0,0.12);
    overflow: hidden;
  }

  /* Front side */
  .card-front {
    top: 35px;
    background: var(--navy);
    color: var(--paper);
  }
  .brand {
    position: absolute;
    left: 0; right: 0; top: 150px;
    display: flex;
    justify-content: center;
    align-items: center;
    gap: 22px;
  }
  .brand-dot {
    width: 64px; height: 64px;
    border-radius: 50%;
    background: var(--paper);
  }
  .brand-name {
    font-family: "Montserrat", Arial, sans-serif;
    font-weight: 400;
    font-size: 46px;
    letter-spacing: 1px;
    text-transform: uppercase;
  }
  .front-url {
    position: absolute;
    left: 0; right: 0; bottom: 70px;
    text-align: center;
    font-family: "Montserrat", Arial, sans-serif;
    font-weight: 400;
    font-size: 15px;
    letter-spacing: 6px;
  }

  /* Back side */
  .card-back {
    top: 465px;
    background: var(--paper);
  }
  .side-band {
    position: absolute;
    left: 0; top: 0; bottom: 0;
    width: 180px;
    background: var(--navy);
  }
  .side-brand {
    position: absolute;
    left: 90px; top: 200px;
    transform: translate(-50%, -50%) rotate(-90deg);
    display: flex;
    align-items: center;
    gap: 14px;
    white-space: nowrap;
    color: var(--paper);
  }
  .side-brand .brand-dot { width: 40px; height: 40px; }
  .side-brand .brand-name { font-size: 28px; }

  .details {
    position: absolute;
    left: 230px; top: 48px;
    color: var(--ink);
  }
  .person-name {
    font-weight: 900;
    font-size: 44px;
    line-height: 1;
    letter-spacing: -0.5px;
  }
  .first-name { color: var(--navy); }
  .last-name { color: var(--grey-name); }
  .role {
    margin-top: 4px;
    font-weight: 300;
    font-size: 24px;
    color: var(--navy);
  }
  .rule {
    width: 50px; height: 3px;
    background: var(--navy);
    margin: 14px 0;
  }
  .address {
    font-weight: 300;
    font-size: 19px;
    line-height: 1.3;
  }
  .contact-list { list-style: none; }
  .contact-list li {
    display: flex;
    align-items: center;
    gap: 14px;
    font-weight: 300;
    font-size: 19px;
    line-height: 1.65;
  }
  .contact-icon { width: 20px; height: 20px; flex: none; }
</style>
</head>
<body>

<section class="card card-front">
  <div class="brand">
    <span class="brand-dot"></span>
    <span class="brand-name">Ward Compass</span>
  </div>
  <p class="front-url">www.wardcompass-example.com</p>
</section>

<section class="card card-back">
  <div class="side-band">
    <div class="side-brand">
      <span class="brand-dot"></span>
      <span class="brand-name">Ward Compass</span>
    </div>
  </div>

  <div class="details">
    <h1 class="person-name"><span class="first-name">Salma</span> <span class="last-name">Derkaoui</span></h1>
    <p class="role">CEO</p>
    <div class="rule"></div>
    <p class="address">14 Annakhil<br>3 H.R.B. Rabat, Morocco</p>
    <div class="rule"></div>
    <ul class="contact-list">
      <li>
        <svg class="contact-icon" viewBox="0 0 20 20" aria-hidden="true">
          <path fill="#163a66" d="M5 2c1 0 2.5 3 2.5 4S6 7.5 6 8.5s2.5 4 5.5 5.5c1 0 1.5-1.5 2.5-1.5S18 14 18 15s-2 3-4 3C8 18 2 12 2 6c0-2 2-4 3-4z"/>
        </svg>
        +90 612 348 2071
      </li>
      <li>
        <svg class="contact-icon" viewBox="0 0 20 20" aria-hidden="true">
          <rect x="1" y="4" width="18" height="12" fill="#163a66"/>
          <path d="M1 4l9 7 9-7" fill="none" stroke="#fff" stroke-width="1.5"/>
        </svg>
        info@wardcompass-example.com
      </li>
      <li>
        <svg class="contact-icon" viewBox="0 0 20 20" aria-hidden="true">
          <circle cx="10" cy="10" r="9" fill="#163a66"/>
          <ellipse cx="10" cy="10" rx="4" ry="9" fill="none" stroke="#fff" stroke-width="1.2"/>
          <path d="M1 10h18M3 5.5h14M3 14.5h14" stroke="#fff" stroke-width="1.2"/>
        </svg>
        www.wardcompass-example.com
      </li>
    </ul>
  </div>
</section>

</body>
</html>
```